Design Business Cards for Quorbel

We need new businesscards for our company called Quorbel. The dimensions is 53mm x 85mm (widht x height), standing, not landscape. We want the businesscards to be creative and original.

On the front side, our company logo, see attached file.
On the backside: a personal photo, name, title, company name, adress, mobile, email and url. Instead of writing ex. "Email", feel free to us a symbol or icon.

Check these three links for inspiration for colours and design;
http://www.plimsoftweb.net/shop/demos/quorbel/
http://www.plimsoftweb.net/shop/demos/quorbel/activities.html
http://www.plimsoftweb.net/shop/demos/quorbel/activity_details.html

```html
<!DOCTYPE html>
<html lang="en">
<head>
<meta charset="utf-8">
<title>Quorbel business cards</title>
<link rel="stylesheet" href="https://fonts.googleapis.com/css2?family=Open+Sans:wght@400;600;700;800&display=swap">
<style>
  :root {
    --backdrop: #d9d9d9;
    --card: #141414;
    --band-address: #262626;
    --band-phone: #2e2e2e;
    --band-email: #363636;
    --band-edge: #414141;
    --accent: #e8431f;
    --accent-deep: #a8321a;
    --white: #ffffff;
    --text-soft: #c9c9c9;
    --text-muted: #8a8a8a;
    --logo-grey: #6e6e6e;
    --avatar: #bdbdbd;
  }
  * { margin: 0; padding: 0; box-sizing: border-box; }
  html, body { width: 1200px; height: 900px; overflow: hidden; }
  body {
    background: var(--backdrop);
    font-family: "Open Sans", Arial, sans-serif;
    position: relative;
  }
  .card {
    position: absolute;
    top: 90px;
    width: 449px;
    height: 720px;
    background: var(--card);
    overflow: hidden;
    box-shadow: 0 10px 30px rgba(0,0,0,0.25);
  }
  .card--front { left: 101px; }
  .card--back { left: 650px; }

  /* front */
  .stripe { position: absolute; left: 0; }
  .stripe--bold { top: 338px; width: 96px; height: 18px; background: var(--accent); }
  .stripe--thin { top: 362px; width: 96px; height: 6px; background: var(--accent-deep); }
  .brand-front {
    position: absolute;
    left: 112px;
    top: 322px;
    color: var(--white);
    font-weight: 800;
    font-size: 50px;
    letter-spacing: 1px;
    line-height: 1;
  }

  /* back */
  .avatar {
    position: absolute;
    left: 174px;
    top: 28px;
    width: 100px;
    height: 100px;
    border-radius: 50%;
    border: 4px solid var(--accent);
    background: radial-gradient(circle at 50% 40%, #d4d4d4, var(--avatar));
  }
  .person {
    position: absolute;
    left: 0;
    top: 144px;
    width: 449px;
    text-align: center;
    white-space: nowrap;
  }
  .person-name {
    color: var(--accent);
    font-weight: 600;
    font-size: 26px;
    letter-spacing: 1px;
    line-height: 1.15;
  }
  .person-title {
    color: var(--text-muted);
    font-size: 9px;
    letter-spacing: 2.5px;
    margin-top: 6px;
  }
  .contact-band {
    position: absolute;
    left: 0;
    width: 449px;
    height: 100px;
    display: flex;
    align-items: center;
    padding-left: 40px;
    color: var(--text-soft);
    font-size: 13px;
    letter-spacing: 0.6px;
    line-height: 1.4;
  }
  .contact-band svg { flex: none; margin-right: 16px; }
  .contact-band--address { top: 240px; background: var(--band-address); }
  .contact-band--phone { top: 340px; background: var(--band-phone); }
  .contact-band--email { top: 440px; background: var(--band-email); }
  .band-edge {
    position: absolute;
    left: 0;
    top: 540px;
    width: 449px;
    height: 36px;
    background: var(--band-edge);
  }
  .brand-back {
    position: absolute;
    left: 0;
    width: 449px;
    top: 630px;
    text-align: center;
    color: var(--logo-grey);
    font-weight: 800;
    font-size: 26px;
    letter-spacing: 1px;
  }
</style>
</head>
<body>
  <section class="card card--front" aria-label="Card front">
    <div class="stripe stripe--bold"></div>
    <div class="stripe stripe--thin"></div>
    <div class="brand-front">QUORBEL</div>
  </section>

  <section class="card card--back" aria-label="Card back">
    <div class="avatar" role="img" aria-label="Personal photo placeholder"></div>
    <div class="person">
      <div class="person-name">YOUR NAME</div>
      <div class="person-title">TITLE GOES HERE</div>
    </div>

    <div class="contact-band contact-band--address">
      <svg width="16" height="16" viewBox="0 0 16 16" aria-hidden="true">
        <path d="M8 1 L15 7 H13 V15 H9.5 V10.5 H6.5 V15 H3 V7 H1 Z" fill="var(--text-soft)"/>
      </svg>
      <span>14 Halden street marrow bay on k4c 2r8<br>ERA/ESA 7483920</span>
    </div>
    <div class="contact-band contact-band--phone">
      <svg width="16" height="16" viewBox="0 0 16 16" aria-hidden="true">
        <path d="M2 5 Q8 1 14 5 L12.5 7 L10.5 6 V5 H5.5 V6 L3.5 7 Z M4 8 H12 L13 14 H3 Z" fill="none" stroke="var(--text-soft)" stroke-width="1.2"/>
        <circle cx="8" cy="11" r="1.6" fill="var(--text-soft)"/>
      </svg>
      <span>000 000 000</span>
    </div>
    <div class="contact-band contact-band--email">
      <svg width="16" height="14" viewBox="0 0 16 14" aria-hidden="true">
        <rect x="1" y="1.5" width="14" height="11" fill="none" stroke="var(--text-soft)" stroke-width="1.2"/>
        <path d="M1 1.5 L8 8 L15 1.5 M1 12.5 L6 7 M15 12.5 L10 7" fill="none" stroke="var(--text-soft)" stroke-width="1.2"/>
      </svg>
      <span>Email : info@brightwayoutings.com</span>
    </div>
    <div class="band-edge"></div>

    <div class="brand-back">QUORBEL</div>
  </section>
</body>
</html>
```